craft brewery needs a 500ml beer bottle label

We need a beer bottle label for a new beer called 'Sunset Mango Haze IPA'
Its based on the movie Half-Court.
We have come up with the name because the beer taste like tropical fruit juice.
So we wanted a tropical theme to the logo.
I have attached one of our old beer labels, but because this will go on larger bottles the dimensions will be -
height=9.75cm
Length= 19cm

I have also attached a rough drawing of what i want the layout of the label to look like, but would like some added material as i am not very creative.
I have also added some other labels which i like the designs of which could be added to this label.
Updates

Target Market(s)

young/ outdoors type/ active/ hipster

Industry/Entity Type

Movie

Colors
33a6d7
ffcf3e
faa54b
f37122
ffffff

Requirements
Must have
• Whats on the attached drawing.
• Stony creek brewing logo which is on one of the attached files
Nice to have
• tropical style/ colourful/ artistic

```html
<!DOCTYPE html>
<html lang="en">
<head>
<meta charset="utf-8">
<title>Sunset Mango Haze IPA – Bottle Label</title>
<link href="https://fonts.googleapis.com/css2?family=Crimson+Pro:ital,wght@1,500&family=Righteous&display=swap" rel="stylesheet">
<style>
  :root {
    --page: #ffffff;
    --ink: #141414;
    --label-orange: #f39322;
    --river-blue: #4a4cf2;
    --title-blue: #3535ea;
    --grass-green: #8dc63f;
    --hop-green: #9fcf55;
    --hop-outline: #1c1c1c;
    --palm-blue: #7474ee;
    --zig-yellow: #ffd21a;
    --zig-red: #e8321e;
    --zig-dark: #2a1a10;
    --white: #ffffff;
  }
  * { margin: 0; padding: 0; box-sizing: border-box; }
  html, body {
    width: 1200px;
    height: 1200px;
    overflow: hidden;
    background: var(--page);
  }
  .canvas {
    position: relative;
    width: 1200px;
    height: 1200px;
  }
  .presentation-caption {
    position: absolute;
    top: 126px;
    left: 0;
    width: 1040px;
    text-align: center;
    font-family: "Crimson Pro", "Palatino Linotype", serif;
    font-style: italic;
    font-weight: 500;
    font-size: 56px;
    color: var(--ink);
  }
  .label {
    position: absolute;
    left: 72px;
    top: 374px;
    width: 1056px;
    height: 542px;
    background: var(--label-orange);
    overflow: hidden;
  }
  .label-art {
    position: absolute;
    inset: 0;
  }
  .section-tag {
    position: absolute;
    left: 38px;
    top: 86px;
    font-family: "Crimson Pro", "Palatino Linotype", serif;
    font-style: italic;
    font-weight: 500;
    font-size: 30px;
    color: var(--white);
  }
  .beer-name {
    position: absolute;
    left: 510px;
    top: 278px;
    font-family: "Righteous", "Arial Black", sans-serif;
    font-size: 58px;
    line-height: 66px;
    color: var(--title-blue);
    letter-spacing: 1px;
  }
  .beer-name .style {
    display: block;
    text-transform: uppercase;
  }
</style>
</head>
<body>
<main class="canvas">
  <p class="presentation-caption">PSD file is ready</p>

  <section class="label">
    <svg class="label-art" width="1056" height="542" viewBox="0 0 1056 542" xmlns="http://www.w3.org/2000/svg">
      <defs>
        <linearGradient id="zigzag-tones" x1="0" y1="0" x2="0" y2="1">
          <stop offset="0" stop-color="var(--zig-yellow)"/>
          <stop offset="0.35" stop-color="#f07a2a"/>
          <stop offset="0.65" stop-color="var(--zig-dark)"/>
          <stop offset="1" stop-color="var(--zig-red)"/>
        </linearGradient>
        <linearGradient id="palm-tones" x1="0" y1="0" x2="0" y2="1">
          <stop offset="0" stop-color="var(--palm-blue)" stop-opacity="0.95"/>
          <stop offset="1" stop-color="var(--palm-blue)" stop-opacity="0.6"/>
        </linearGradient>
      </defs>

      <rect class="zigzag-band" role="img" aria-label="Band of yellow, orange, black and red zigzag stripes"
            x="0" y="6" width="1056" height="44" fill="url(#zigzag-tones)" opacity="0.55"/>

      <path class="river-line" d="M762 0 C738 96 668 172 540 194 C408 206 283 228 218 326 C204 356 202 386 202 516"
            fill="none" stroke="var(--river-blue)" stroke-width="27"/>

      <rect class="grass-band" x="0" y="516" width="1056" height="26" fill="var(--grass-green)"/>

      <ellipse class="hop-cone" role="img" aria-label="Green hop cone illustration"
               cx="540" cy="172" rx="46" ry="56" fill="var(--hop-green)" stroke="var(--hop-outline)" stroke-width="3"/>

      <rect class="palm-tree" role="img" aria-label="Blue palm tree silhouette"
            x="376" y="242" width="116" height="200" rx="40" fill="url(#palm-tones)"/>
    </svg>

    <p class="section-tag">About Beer</p>

    <h1 class="beer-name">sunset mango<br>haze<span class="style">IPA</span></h1>
  </section>
</main>
</body>
</html>
```